A simple Chatterbook Ad (not Chatterbook Page) for weight loss surgery

It’s a simple ad in terms of the text.

The text should say:
Curious about weight loss surgery?
This 30 second quiz will tell you which procedure will suit you best

I'm open to variations in the text if it is thought to enhance the ad.

Targeted towards obese individuals who have been unable to lose weight with diet and exercise. My industry is weight loss surgery – webpage www.marcusbellweather.com.au. Clicking the ad leads to a quiz on my webpage relating to weight loss surgery. Most frequent users of this service are females (75%) between ages of 35 and 55 years.

Successful weight loss surgery can enable individuals who have been unable to lose weight to lose a substantial amount of the excess weight they are carrying to be healthier and happier.

```html
<!DOCTYPE html>
<html lang="en">
<head>
<meta charset="utf-8">
<title>Weight Loss Surgery Quiz Ad</title>
<link rel="stylesheet" href="https://fonts.googleapis.com/css2?family=Red+Hat+Display:wght@400;500;700;800&family=Cinzel:wght@500&display=swap">
<style>
  :root {
    --teal: #00a69c;
    --teal-dark: #12a49a;
    --cyan: #00bcd6;
    --white: #ffffff;
    --purple: #8b3a8a;
    --salmon: #f58f77;
    --pink: #ec2a7b;
    --yellow: #f3d179;
    --red: #dd3a4a;
    --green: #8cc63f;
    --grey: #6d6e71;
  }
  * { margin: 0; padding: 0; box-sizing: border-box; }
  html, body { width: 1200px; height: 1200px; overflow: hidden; background: var(--white); }
  body { font-family: "Red Hat Display", Arial, sans-serif; position: relative; }

  .header-band {
    position: absolute; left: 0; top: 60px; width: 1200px; height: 207px;
    background: var(--teal);
    display: flex; align-items: center; padding-left: 78px;
  }
  .headline { color: var(--white); font-size: 49px; font-weight: 400; letter-spacing: -0.5px; }
  .headline strong { font-weight: 800; }

  .pitch {
    position: absolute; left: 78px; top: 385px;
    color: var(--teal); font-size: 58px; font-weight: 400; line-height: 79px; letter-spacing: -0.5px;
  }

  .quiz-visual {
    position: absolute; left: 735px; top: 300px; width: 410px; height: 410px;
    border-radius: 50%;
    background: radial-gradient(circle, #27c3da 0%, #7fd9e8 55%, #e6f7fa 100%);
    display: flex; flex-direction: column; align-items: center; justify-content: center;
    color: var(--white);
  }
  .quiz-visual .seconds { font-size: 64px; font-weight: 800; line-height: 1; }
  .quiz-visual .unit { font-size: 30px; font-weight: 700; letter-spacing: 6px; }

  .procedure-band {
    position: absolute; left: 0; top: 734px; width: 1200px; height: 284px;
    background: var(--cyan);
  }
  .procedure-band svg { position: absolute; left: 0; top: 0; }
  .procedure-card {
    position: absolute; left: 37px; top: 36px; width: 1126px; height: 201px;
    background: var(--white); border-radius: 24px;
  }
  .pill {
    position: absolute; height: 32px; border-radius: 16px;
    color: var(--white); font-size: 22px; font-weight: 500;
    display: flex; align-items: center; justify-content: center; white-space: nowrap;
  }
  .pill.sleeve   { left: 23px;  top: 57px; width: 274px; background: var(--purple); }
  .pill.banding  { left: 326px; top: 57px; width: 256px; background: var(--salmon); }
  .pill.revision { left: 611px; top: 57px; width: 273px; background: var(--cyan); }
  .pill.liner    { left: 923px; top: 57px; width: 174px; background: var(--pink); }
  .pill.bypass   { left: 23px;  top: 115px; width: 274px; background: var(--yellow); }
  .pill.contour  { left: 326px; top: 115px; width: 388px; background: var(--red); }
  .pill.balloon  { left: 747px; top: 115px; width: 355px; background: var(--green); }

  .brand { position: absolute; left: 78px; top: 1080px; display: flex; align-items: center; gap: 16px; }
  .brand-dot { width: 62px; height: 62px; border-radius: 50%; background: var(--teal); }
  .brand-name { color: var(--teal-dark); font-size: 36px; font-weight: 700; letter-spacing: 1px; line-height: 1; }
  .brand-role { color: var(--grey); font-size: 14px; font-weight: 500; letter-spacing: 2.4px; text-transform: uppercase; margin-top: 6px; }

  .contact { position: absolute; right: 50px; top: 1066px; text-align: right; color: var(--teal); }
  .contact-label { font-size: 22px; font-weight: 500; }
  .contact-phone { font-size: 58px; font-weight: 500; line-height: 1.1; letter-spacing: -0.5px; }
</style>
</head>
<body>
  <header class="header-band">
    <h1 class="headline">Curious about <strong>WEIGHT LOSS SURGERY?</strong></h1>
  </header>

  <p class="pitch">This 30 second quiz will<br>tell you which procedure<br>will suit you best.</p>

  <div class="quiz-visual" role="img" aria-label="Light bulb illustration with colourful rays and a 30 second timer">
    <span class="seconds">30</span>
    <span class="unit">sec</span>
  </div>

  <section class="procedure-band">
    <svg width="1200" height="40" viewBox="0 0 1200 40" aria-hidden="true">
      <polygon points="953,0 1020,0 1015,40 880,40" fill="#ffffff"/>
    </svg>
    <div class="procedure-card">
      <span class="pill sleeve">Sleeve Gastrectomy</span>
      <span class="pill banding">Gastric Banding</span>
      <span class="pill revision">Revision &amp; Reversal</span>
      <span class="pill liner">Duodenal Liner</span>
      <span class="pill bypass">Gastric Bypass</span>
      <span class="pill contour">Body Contouring for Loose Skin</span>
      <span class="pill balloon">Gastric Balloon Implantation</span>
    </div>
  </section>

  <footer>
    <div class="brand">
      <span class="brand-dot"></span>
      <div>
        <div class="brand-name">MARCUS BELLWEATHER</div>
        <div class="brand-role">General, Upper GI &amp; Bariatric Surgeon</div>
      </div>
    </div>
    <div class="contact">
      <div class="contact-label">For all appointments</div>
      <div class="contact-phone">03 9000 4127</div>
    </div>
  </footer>
</body>
</html>
```